Website customization using WordPress Theme already purchased

Need informational website for Orla Brightwell LLC. Orla Brightwell is investment group company for multiple cloud based products and website. We need website for anyone coming to our website to be able get information on our products. I already have WordPress theme that I would like to use. Right person/company will be able to customize WordPress theme to our needs and be able to give us final product of 7-9 pages of complete website.

Industry/Entity Type

Investment

Number of Pages Required

5+ page

Colors
add136
3176b5
ec1f27
f37122

```html
<!DOCTYPE html>
<html lang="en">
<head>
<meta charset="utf-8">
<title>Orla Brightwell LLC</title>
<link href="https://fonts.googleapis.com/css2?family=Oswald:wght@300;400&family=Open+Sans:wght@400;600;700&display=swap" rel="stylesheet">
<style>
:root{
  --navy:#20306b;
  --blue:#0066b3;
  --title-blue:#1f6fb5;
  --ink:#1b1b1b;
  --muted:#6a6a6a;
  --paper:#f7f7f7;
  --red:#ec1f27;
  --brown:#5a3220;
  --leaf:#add136;
}
*{margin:0;padding:0;box-sizing:border-box}
html,body{width:672px;height:1200px;overflow:hidden}
body{font-family:"Open Sans",sans-serif;color:var(--ink);position:relative;background:#fff}
.abs{position:absolute}
.hero{left:0;top:0;width:672px;height:421px;background:linear-gradient(180deg,#cfe4e4 0%,#dfe8dc 45%,#efe2c2 80%,#e9d6b0 100%)}
.hero-photo{position:absolute;left:300px;top:60px;width:372px;height:361px;background:radial-gradient(ellipse at 55% 55%,rgba(120,110,80,.45) 0%,rgba(200,160,120,.35) 40%,rgba(0,0,0,0) 70%)}
.brand{left:97px;top:28px;display:flex;align-items:center;gap:6px}
.brand-dot{width:36px;height:36px;border-radius:50%;background:var(--title-blue)}
.brand-name{font-weight:700;font-size:12px;color:var(--navy)}
.nav{left:337px;top:38px;display:flex;gap:10px;font-size:9.5px;font-weight:700}
.nav a{color:var(--ink);text-decoration:none}
.nav .active{border-bottom:1.5px solid var(--navy);padding-bottom:2px}
.social{left:545px;top:38px;display:flex;gap:6px}
.social span{width:9px;height:9px;border-radius:50%;background:var(--leaf)}
.hero-title{left:97px;top:167px;font-family:"Oswald",sans-serif;font-size:29px;line-height:32px;color:var(--title-blue);font-weight:400;white-space:nowrap}
.hero-text{left:97px;top:201px;width:215px;font-size:8.6px;line-height:12px;color:#333}
.btn{left:97px;top:230px;width:64px;height:33px;border-radius:8px;background:var(--navy);color:#fff;font-size:6px;display:flex;align-items:center;justify-content:center}
.dots{left:435px;top:370px;display:flex;gap:2px}
.dots span{width:7px;height:7px;border-radius:50%;background:#999}
.dots span:first-child{background:#fff}
.band{left:0;top:421px;width:672px;height:165px;background:var(--navy)}
.pillar{position:absolute;top:38px;width:112px;color:#fff}
.pillar h2{font-family:"Oswald",sans-serif;font-weight:400;font-size:15px;line-height:20px;margin-bottom:1px}
.pillar p{font-size:7.4px;line-height:12px;color:#d7dbea}
.pillar .more{display:block;text-align:right;font-family:"Oswald",sans-serif;font-weight:300;font-size:9px;margin-top:8px;color:#fff}
.pillar .more b{color:#4d8fd8;font-weight:400}
.middle{left:0;top:586px;width:672px;height:222px;background:var(--paper);box-shadow:inset 0 4px 6px rgba(0,0,0,.08)}
.card{left:109px;top:51px;width:213px;height:125px;background:#fff;box-shadow:0 1px 4px rgba(0,0,0,.18)}
.avatar{left:97px;top:60px;width:25px;height:25px;border-radius:50%;background:linear-gradient(#9a9a9a,#5a5a5a)}
.card h3{position:absolute;left:20px;top:13px;font-family:"Oswald",sans-serif;font-weight:400;font-size:15px;line-height:20px}
.card p{position:absolute;left:20px;top:36px;width:172px;font-size:7.6px;line-height:12px;color:#444}
.card-dots{left:207px;top:183px;display:flex;gap:2px}
.card-dots span{width:7px;height:7px;border-radius:50%;border:1px solid #aaa;background:#fff}
.card-dots span:first-child{background:#555;border-color:#555}
.news{left:352px;top:64px;width:200px}
.news h3{font-family:"Oswald",sans-serif;font-weight:400;font-size:15px;line-height:20px;margin-bottom:6px}
.news h4{font-size:7.8px;font-weight:700;margin-top:5px}
.news p{font-size:7.8px;color:var(--muted)}
.partners{left:0;top:808px;width:672px;height:84px;background:#f9f9f9;border-top:1px solid #e6e6e6}
.partner{position:absolute;top:34px;transform:translateX(-50%);display:flex;align-items:center;gap:5px;font-size:13px;font-weight:600;color:#555;white-space:nowrap}
.partner i{display:block;width:13px;height:13px}
.footer{left:0;top:892px;width:672px;height:250px;background:var(--blue)}
.fcol{position:absolute;top:47px;width:145px}
.fcol h2{font-family:"Oswald",sans-serif;font-weight:300;font-size:15px;line-height:20px;color:var(--brown);margin-bottom:2px}
.fcol p{font-size:7.6px;line-height:14px;color:#dfeaf6}
.newsletter{left:436px;top:55px;width:139px;height:154px;background:#fff;border:1.5px solid var(--red);text-align:center}
.newsletter svg{margin-top:8px}
.newsletter h5{font-family:"Oswald",sans-serif;font-weight:400;font-size:7px;color:#333;margin-top:2px}
.field{margin:3px auto 0;width:122px;height:15px;border:1.3px solid var(--red);font-size:8px;color:#888;text-align:left;padding-left:3px;line-height:13px}
.subscribe{margin:8px auto 0;width:60px;height:22px;background:#ec4a50;color:#fff;font-size:10px;line-height:22px}
.mini{display:flex;gap:4px;justify-content:center;margin-top:6px}
.mini span{width:6px;height:6px;border-radius:50%;background:var(--navy)}
.bottom{left:0;top:1142px;width:672px;height:58px;background:linear-gradient(90deg,#1a2430,#243142 50%,#1a2430)}
.bottom nav{position:absolute;left:97px;top:29px;display:flex;gap:11px;font-size:8px;color:#fff}
.bottom .active{color:#3a8fe0;font-weight:700}
</style>
</head>
<body>
<header class="abs hero">
  <div class="hero-photo" role="img" aria-label="Photo of cupped hands holding soil with a young tree growing from it"></div>
  <div class="abs brand"><span class="brand-dot"></span><span class="brand-name">Orla Brightwell</span></div>
  <nav class="abs nav"><a class="active">Home</a><a>Portfolio</a><a>Company</a><a>Contact Us</a></nav>
  <div class="abs social"><span></span><span></span></div>
  <h1 class="abs hero-title">Orla Brightwell LLC</h1>
  <p class="abs hero-text">Orla Brightwell is investment group company for multiple cloud based products and website.</p>
  <div class="abs btn">READ MORE</div>
  <div class="abs dots"><span></span><span></span></div>
</header>

<section class="abs band">
  <div class="pillar" style="left:129px"><h2>OUR MISSION</h2><p>It is a long established fact that a reader will be distracted by the readable content of a page when looking at its layout.</p><span class="more">READ MORE <b>›</b></span></div>
  <div class="pillar" style="left:296px"><h2>WHO WE ARE</h2><p>It is a long established fact that a reader will be distracted by the readable content of a page when looking at its layout.</p><span class="more">READ MORE <b>›</b></span></div>
  <div class="pillar" style="left:463px"><h2>WHAT WE DO</h2><p>It is a long established fact that a reader will be distracted by the readable content of a page when looking at its layout.</p><span class="more">READ MORE <b>›</b></span></div>
</section>

<section class="abs middle">
  <div class="abs card">
    <h3>MARA ELLISON</h3>
    <p>Mara manages the firm's operations, organizes special events and assists in portfolio activities. Prior to Corvane Cloud, Mara spent nine years at Brightlane as a Sr. Executive Administrator supporting Tomas. Mara earned her Bachelors from Westbridge State University.</p>
  </div>
  <div class="abs avatar" role="img" aria-label="Portrait photo of team member"></div>
  <div class="abs card-dots"><span></span><span></span></div>
  <div class="abs news">
    <h3>RECENT NEWS</h3>
    <h4>Orla Brightwell LLC</h4><p>Posted by admin on Nov 1, 2016 in Sliders</p>
    <h4 style="margin-top:8px">INVESTING IN PEOPLE</h4><p>Posted by admin on Nov 1, 2016 in Sliders</p>
  </div>
</section>

<section class="abs partners">
  <div class="partner" style="left:145px"><i style="background:#e6d54a;border-radius:50%"></i>Citrine</div>
  <div class="partner" style="left:270px"><i style="background:#d9342b"></i>Lattice Works</div>
  <div class="partner" style="left:394px"><i style="background:#2a9fd8"></i>Taskly</div>
  <div class="partner" style="left:520px"><i style="background:#3c7a3e;border-radius:50%"></i>Fernleaf</div>
</section>

<footer class="abs footer">
  <div class="fcol" style="left:97px"><h2>ABOUT US</h2><p>&nbsp; focuses on seed to later stage companies building infrastructure and value chains around data. We love Technology heavy companies gathering or creating unique data at every stage of the data stack — from infrastructure all the way to applications, mobile, and sensors.</p></div>
  <div class="fcol" style="left:266px;width:140px"><h2>CONTACT</h2><p>The best way to reach us is through an introduction from our network, or our official address will be replaced If you wish to grab our attention just provide a single sentence on what you do, and links to your Pitch Deck, Linkfolio profile, and Codeshelf account. For press enquires please contact</p></div>
  <div class="abs newsletter">
    <svg width="15" height="11" viewBox="0 0 15 11"><rect x="0.75" y="0.75" width="13.5" height="9.5" fill="none" stroke="#333" stroke-width="1.3"/><path d="M1 1l6.5 5 6.5-5" fill="none" stroke="#333" stroke-width="1.3"/></svg>
    <h5>GET MONTHLY NEWSLETTER</h5>
    <div class="field">First Name</div>
    <div class="field">Last Name</div>
    <div class="field">Email</div>
    <div class="subscribe">Subscribe</div>
    <div class="mini"><span></span><span></span><span></span><span></span><span></span></div>
  </div>
</footer>

<div class="abs bottom">
  <nav><span class="active">Home</span><span>Company</span><span>Contact Us</span><span>Portfolio</span></nav>
</div>
</body>
</html>
```